Business Card Design Project

Business Card
We are rebranding with a new logo
Industry/Entity Type
Business
Contact Information for Business Card
Dennis Marlow +61 427581962 dennis@qovo.com.au P.O. Box 872 Kelvindale QLD 4309
Requirements
Must have
- Logo

```html
<!DOCTYPE html>
<html lang="en">
<head>
<meta charset="utf-8">
<title>Qovo International – Business Card</title>
<link rel="stylesheet" href="https://fonts.googleapis.com/css2?family=Arimo:wght@400;700&family=Roboto+Condensed:wght@500&display=swap">
<style>
  :root {
    --backdrop: #cdc1a9;
    --card-white: #ffffff;
    --panel-grey: #e6e7e8;
    --brand-blue: #1895cb;
    --text-white: #ffffff;
    --accent-orange: #f0821e;
  }
  * { box-sizing: border-box; margin: 0; padding: 0; }
  html, body {
    width: 1200px;
    height: 900px;
    overflow: hidden;
    background: var(--backdrop);
  }
  .business-card {
    position: absolute;
    left: 150px;
    top: 190px;
    width: 900px;
    height: 520px;
    background: var(--card-white);
    box-shadow: 0 18px 40px rgba(60, 45, 20, 0.25);
    overflow: hidden;
  }
  .grey-band {
    position: absolute;
    top: 0;
    right: 0;
    width: 38%;
    height: 100%;
    background: var(--panel-grey);
  }
  .contact-panel {
    position: absolute;
    left: 51%;
    right: 2.5%;
    top: 15%;
    bottom: 13%;
    background: var(--brand-blue);
    color: var(--text-white);
    padding: 62px 0 0 72px;
  }
  .contact-name {
    font-family: "Roboto Condensed", "Arial Narrow", sans-serif;
    font-weight: 500;
    font-size: 36px;
    letter-spacing: 0.2px;
    margin-bottom: 22px;
  }
  .contact-details {
    font-family: "Arimo", Arial, sans-serif;
    font-size: 21px;
    line-height: 1.3;
    list-style: none;
  }
  .brand-mark {
    position: absolute;
    left: 110px;
    top: 190px;
    display: flex;
    align-items: center;
    gap: 18px;
  }
  .brand-dot {
    width: 46px;
    height: 46px;
    border-radius: 50%;
    background: var(--accent-orange);
    flex: none;
  }
  .brand-name {
    font-family: "Arimo", Arial, sans-serif;
    font-weight: 700;
    color: var(--brand-blue);
    line-height: 1;
  }
  .brand-name .brand-word {
    display: block;
    font-size: 74px;
    letter-spacing: 1px;
  }
  .brand-name .brand-sub {
    display: block;
    font-size: 22px;
    letter-spacing: 6px;
    margin-top: 8px;
  }
</style>
</head>
<body>
  <article class="business-card">
    <div class="grey-band"></div>

    <div class="brand-mark">
      <span class="brand-dot"></span>
      <p class="brand-name">
        <span class="brand-word">Qovo</span>
        <span class="brand-sub">INTERNATIONAL</span>
      </p>
    </div>

    <section class="contact-panel">
      <h1 class="contact-name">Dennis Marlow</h1>
      <ul class="contact-details">
        <li>+61 427581962</li>
        <li>dennis@qovo.com.au</li>
        <li>P.O. Box 872</li>
        <li>Kelvindale QLD 4309</li>
      </ul>
    </section>
  </article>
</body>
</html>
```